Granite Peak Roofing & Exteriors Ltd

I would like to start a Facebook page for business that outlines granite peak roofing . We have been in business since 2005 & have completed more than 5000 projects . Our company is area licensed, insured , covered by qlf , ntz member , journey man roofers , offer financing, zero down payment required , free quotes , serving red deer & area .

Please do not put years on the homepage.

Target Market(s)

Roofers in red deer & central Alberta

Industry/Entity Type

Roofing

Requirements
Must have
• Shingles , soffit , fascia , siding , gutters , roof repair , exterior painting , exterior washing .

```html
<!DOCTYPE html>
<html lang="en">
<head>
<meta charset="utf-8">
<title>Granite Peak Roofing &amp; Exteriors Ltd — Facebook Cover</title>
<link rel="stylesheet" href="https://fonts.googleapis.com/css2?family=Anton&family=Oswald:wght@500;600&display=swap">
<style>
  :root {
    --brand-red: #b3121f;
    --ink: #111111;
    --paper: #ffffff;
    --page-bg: #e9ecf1;
    --badge-cream: #fbf7e6;
    --badge-navy: #1f5a92;
  }
  html, body {
    margin: 0;
    width: 1200px;
    height: 900px;
    overflow: hidden;
    background: var(--page-bg);
  }
  .cover {
    position: absolute;
    left: 30px;
    top: 239px;
    width: 1140px;
    height: 422px;
    background: var(--paper);
    overflow: hidden;
    box-shadow: 0 6px 24px rgba(0,0,0,.12);
  }
  .cover__photos {
    position: absolute;
    inset: 0;
  }
  .headline {
    position: absolute;
    left: 58px;
    top: 30px;
    margin: 0;
    font-family: "Anton", "Oswald", sans-serif;
    font-weight: 400;
    font-size: 40px;
    line-height: 42px;
    color: var(--brand-red);
    letter-spacing: 0.2px;
    text-transform: uppercase;
  }
  .services {
    position: absolute;
    left: 57px;
    top: 168px;
    margin: 0;
    padding: 0;
    list-style: none;
    display: grid;
    grid-template-columns: 106px 88px 107px 150px;
    grid-auto-flow: column;
    grid-template-rows: 24px 24px;
    font-family: "Oswald", sans-serif;
    font-weight: 500;
    font-size: 21px;
    color: var(--ink);
  }
  .services li {
    display: flex;
    align-items: center;
    gap: 3px;
    white-space: nowrap;
    line-height: 24px;
  }
  .tick {
    width: 18px;
    height: 18px;
    flex: none;
  }
  .offer-bar {
    position: absolute;
    left: 55px;
    top: 228px;
    width: 447px;
    height: 31px;
    background: var(--brand-red);
    color: var(--paper);
    font-family: "Oswald", sans-serif;
    font-weight: 600;
    font-size: 18px;
    line-height: 31px;
    text-align: center;
    text-transform: uppercase;
    letter-spacing: -0.2px;
  }
  .service-area {
    position: absolute;
    left: 52px;
    top: 266px;
    margin: 0;
    font-family: "Anton", sans-serif;
    font-weight: 400;
    font-size: 46px;
    line-height: 54px;
    color: var(--ink);
    text-transform: uppercase;
  }
  .credentials {
    position: absolute;
    left: 42px;
    top: 362px;
    width: 235px;
    height: 48px;
    background: var(--badge-cream);
    display: flex;
    align-items: center;
    gap: 10px;
    padding: 0 12px;
    box-sizing: border-box;
  }
  .credentials__board {
    width: 120px;
    height: 28px;
    background: #d9dce2;
    border-radius: 3px;
  }
  .credentials__member {
    width: 78px;
    height: 36px;
    background: var(--badge-navy);
    border-radius: 2px;
  }
  .phone {
    position: absolute;
    left: 297px;
    top: 340px;
    display: flex;
    align-items: center;
    gap: 10px;
    font-family: "Anton", sans-serif;
    font-size: 35px;
    line-height: 40px;
    color: var(--brand-red);
  }
  .phone__icon {
    width: 34px;
    height: 34px;
  }
  .website {
    position: absolute;
    left: 297px;
    top: 382px;
    height: 21px;
    display: flex;
    font-family: "Oswald", sans-serif;
    font-weight: 600;
    font-size: 14px;
    line-height: 21px;
    color: var(--paper);
  }
  .website__label {
    background: var(--brand-red);
    padding: 0 6px;
  }
  .website__url {
    background: var(--ink);
    padding: 0 7px;
  }
</style>
</head>
<body>
  <section class="cover" aria-label="Granite Peak Roofing &amp; Exteriors Ltd cover banner">
    <svg class="cover__photos" viewBox="0 0 1140 422" width="1140" height="422">
      <defs>
        <linearGradient id="house-photo" x1="0" y1="0" x2="0.3" y2="1">
          <stop offset="0" stop-color="#c3ccd6"/>
          <stop offset="0.35" stop-color="#8a8f96"/>
          <stop offset="0.7" stop-color="#9a3a3c"/>
          <stop offset="1" stop-color="#5b2a22"/>
        </linearGradient>
        <linearGradient id="wrap-photo" x1="0" y1="0" x2="1" y2="1">
          <stop offset="0" stop-color="#a9b4bb"/>
          <stop offset="1" stop-color="#d7dde0"/>
        </linearGradient>
        <linearGradient id="window-photo" x1="0" y1="0" x2="1" y2="1">
          <stop offset="0" stop-color="#8fb0d4"/>
          <stop offset="1" stop-color="#c6d4e3"/>
        </linearGradient>
      </defs>
      <polygon role="img" aria-label="Photo: roof under construction with house wrap above a snowy yard"
               points="708,0 906,0 795,200 643,123" fill="url(#wrap-photo)"
               stroke="var(--brand-red)" stroke-width="3"/>
      <polygon role="img" aria-label="Photo: close-up of a house gable with large windows"
               points="643,123 795,200 720,330 547,282" fill="url(#window-photo)"
               stroke="var(--brand-red)" stroke-width="3"/>
      <polygon role="img" aria-label="Photo: red-sided house with a new grey shingle roof"
               points="910,0 1140,0 1140,422 667,422" fill="url(#house-photo)"/>
      <line x1="910" y1="0" x2="667" y2="422" stroke="var(--brand-red)" stroke-width="4"/>
    </svg>

    <svg width="0" height="0" style="position:absolute">
      <symbol id="icon-tick" viewBox="0 0 20 20">
        <circle cx="10" cy="10" r="8" fill="none" stroke="#b3121f" stroke-width="2"/>
        <path d="M5.5 10.5 L9 14 L18 3" fill="none" stroke="#b3121f" stroke-width="2.4" stroke-linecap="round" stroke-linejoin="round"/>
      </symbol>
    </svg>

    <h1 class="headline">We specialize in residential,<br>commercial &amp; industrial<br>roofing and exteriors</h1>

    <ul class="services">
      <li><svg class="tick"><use href="#icon-tick"/></svg>Shingles</li>
      <li><svg class="tick"><use href="#icon-tick"/></svg>Soffit</li>
      <li><svg class="tick"><use href="#icon-tick"/></svg>Fascia</li>
      <li><svg class="tick"><use href="#icon-tick"/></svg>Siding</li>
      <li><svg class="tick"><use href="#icon-tick"/></svg>Gutters</li>
      <li><svg class="tick"><use href="#icon-tick"/></svg>Roof repair</li>
      <li><svg class="tick"><use href="#icon-tick"/></svg>Exterior painting</li>
      <li><svg class="tick"><use href="#icon-tick"/></svg>Exterior washing</li>
    </ul>

    <div class="offer-bar">Financing, zero down payment required , free quotes</div>

    <p class="service-area">Serving Red Deer &amp; Area</p>

    <div class="credentials">
      <span class="credentials__board" role="img" aria-label="QLF coverage badge"></span>
      <span class="credentials__member" role="img" aria-label="NTZ member badge"></span>
    </div>

    <div class="phone">
      <svg class="phone__icon" viewBox="0 0 34 34" aria-hidden="true">
        <circle cx="17" cy="17" r="15" fill="none" stroke="var(--brand-red)" stroke-width="2.5"/>
        <path d="M11 9.5c1-.8 2-.6 2.6.3l1.6 2.6c.5.8.3 1.7-.4 2.2l-1.2.9c.9 2.1 2.6 3.8 4.7 4.8l.9-1.2c.5-.7 1.5-.9 2.2-.4l2.6 1.6c.9.6 1.1 1.6.3 2.6l-1 1.2c-.9 1-2.4 1.3-3.7.8-4.4-1.8-7.8-5.2-9.6-9.6-.5-1.3-.2-2.8.8-3.7z" fill="var(--brand-red)"/>
      </svg>
      <span>403. 555. 0187</span>
    </div>

    <div class="website">
      <span class="website__label">Our Website</span>
      <span class="website__url">www.granitepeakroofing.ca</span>
    </div>
  </section>
</body>
</html>
```